Business Card Design Project

I need a business card design for my freelance solo makeup artistry business in Melbourne, Australia called Rosa Marindi. My freelance business specialises in bridal and special occassions makeup.

I like the idea of having Rosa Marindi in pink as its a feminine and soft colour. I would like a very clean, classy and simple (with an element of fun if that's possible) design. I would consider the business name to be in gloss with an otherwise matte finish.

Underneath the business name, I would like "Makeup by Tessa Colwick"

I do not want any bridal related graphics.

Target Market(s)

Young females with a disposable income from ages 20-40 and females getting married who will dictate who does mother of bride makeup ages 40-70.

Industry/Entity Type

Business

Requirements
Must have
• "Makeup by Tessa Colwick"

Ph: 0412 385 604
E: rosamarindi@inboxly.net
ABN: 58204917362
Nice to have
• I think I would like a mini business cards which is more slimline. I do like the colours of pink, white and grey but open to suggestions.
Should not have
• Bridal related graphics

```html
<!DOCTYPE html>
<html lang="en">
<head>
<meta charset="utf-8">
<title>Rosa Marindi – Business Card</title>
<link rel="stylesheet" href="https://fonts.googleapis.com/css2?family=Nothing+You+Could+Do&family=Varela+Round&display=swap">
<style>
  :root {
    --paper: #ffffff;
    --frame: #0d0d0d;
    --blush: #f08c84;
    --blush-soft: #f6b3ac;
    --blush-mist: #fbe2df;
    --ink: #111111;
    --slate: #747474;
    --steel: #d4d4d4;
  }
  * { box-sizing: border-box; margin: 0; padding: 0; }
  html, body {
    width: 1200px; height: 628px; overflow: hidden;
    background: var(--paper);
  }
  .card {
    position: relative;
    width: 1200px; height: 628px;
    background: var(--paper);
    font-family: "Varela Round", sans-serif;
  }
  .card__frame {
    position: absolute;
    left: 18px; top: 18px; right: 18px; bottom: 18px;
    border: 8px solid var(--frame);
    border-radius: 34px;
  }
  .card__brush {
    position: absolute;
    left: 700px; top: 62px;
    width: 475px; height: 44px;
    border-radius: 22px 4px 4px 22px;
    background: linear-gradient(90deg, var(--blush-soft) 0%, var(--steel) 35%, var(--steel) 100%);
  }
  .card__swash {
    position: absolute;
    left: 62px; top: 290px;
    width: 1090px; height: 125px;
    border-radius: 60px;
    background: linear-gradient(180deg, var(--paper) 0%, var(--blush-mist) 55%, var(--paper) 100%);
  }
  .card__name {
    position: absolute;
    left: 66px; top: 112px;
    font-size: 132px;
    font-weight: 400;
    line-height: 1;
    color: var(--blush);
    white-space: nowrap;
  }
  .card__pencil {
    position: absolute;
    left: 30px; top: 432px;
    width: 912px; height: 76px;
    background: var(--ink);
  }
  .card__tagline {
    position: absolute;
    left: 110px; top: 448px;
    color: var(--paper);
    font-size: 33px;
    line-height: 44px;
    white-space: nowrap;
  }
  .card__artist {
    font-family: "Nothing You Could Do", cursive;
    color: var(--blush-soft);
    font-size: 36px;
    font-weight: 700;
    margin-left: 14px;
  }
  .card__contacts {
    position: absolute;
    left: 0; top: 544px;
    width: 100%;
    font-size: 28px;
    font-style: normal;
    color: var(--slate);
    white-space: nowrap;
  }
  .card__contact { position: absolute; top: 0; }
  .card__contact--phone { left: 112px; }
  .card__contact--email { left: 412px; }
  .card__contact--abn { left: 842px; }
</style>
</head>
<body>
  <main class="card">
    <div class="card__frame"></div>

    <div class="card__brush" role="img" aria-label="Lip gloss applicator wand with pink gloss on the tip"></div>

    <div class="card__swash" role="img" aria-label="Flowing pink swash flourish underlining the business name"></div>

    <h1 class="card__name">Rosa Marindi</h1>

    <div class="card__pencil" role="img" aria-label="Black eyeliner pencil with a sharpened tip"></div>
    <p class="card__tagline">makeup by<span class="card__artist">Tessa Colwick</span></p>

    <address class="card__contacts">
      <span class="card__contact card__contact--phone">Ph: 0412 385 604</span>
      <span class="card__contact card__contact--email">E: rosamarindi@inboxly.net</span>
      <span class="card__contact card__contact--abn">ABN: 58204917362</span>
    </address>
  </main>
</body>
</html>
```